Business Cards and Stationery for a laboratory quality consulting business
Brennick Quality Solutions
Creative Brief
Simple
Marion Brennick
Principal Consultant
4817 Thistlewood Lane Cary, NC 27604
marion@brennickquality.example
www.brennickquality.example

```html
<!DOCTYPE html>
<html lang="en">
<head>
<meta charset="utf-8">
<title>Brennick Quality Solutions – Business Card</title>
<link rel="stylesheet" href="https://fonts.googleapis.com/css2?family=Montserrat:wght@500;600;700;800&display=swap">
<style>
  :root {
    --teal: #0e8c86;
    --orange: #f7a21b;
    --card: #ffffff;
    --backdrop: #ececec;
    --white: #ffffff;
  }
  * { margin: 0; padding: 0; box-sizing: border-box; }
  html, body {
    width: 1200px;
    height: 818px;
    overflow: hidden;
    background: var(--backdrop);
    font-family: "Montserrat", sans-serif;
  }
  .business-card {
    position: absolute;
    left: 160px;
    top: 84px;
    width: 880px;
    height: 650px;
    background: var(--card);
    overflow: hidden;
  }
  .accent-bar-left {
    position: absolute;
    left: 10px;
    top: 71px;
    width: 46px;
    height: 128px;
    background: var(--orange);
  }
  .brand {
    position: absolute;
    left: 70px;
    top: 74px;
    display: flex;
    align-items: center;
    gap: 14px;
  }
  .brand-dot {
    width: 92px;
    height: 92px;
    border-radius: 50%;
    background: var(--orange);
    flex-shrink: 0;
  }
  .brand-name {
    color: var(--teal);
    font-weight: 800;
    line-height: 1;
  }
  .brand-name .primary { display: block; font-size: 60px; letter-spacing: -1px; }
  .brand-name .secondary { display: block; font-size: 21px; margin-top: 6px; }
  .name-bar {
    position: absolute;
    left: 490px;
    top: 71px;
    width: 390px;
    height: 131px;
    background: var(--orange);
    color: var(--white);
    text-align: right;
    padding: 35px 32px 0 0;
  }
  .person-name { font-size: 32px; font-weight: 600; line-height: 1.1; }
  .person-title { font-size: 16px; font-weight: 600; margin-top: 6px; }
  .contact {
    position: absolute;
    left: 30px;
    top: 392px;
    font-size: 23px;
    font-weight: 600;
    line-height: 36px;
  }
  .contact .address { color: var(--orange); margin-bottom: 10px; }
  .contact .line { color: var(--teal); margin-bottom: 9px; line-height: 36px; }
  .footer-bands {
    position: absolute;
    left: 0;
    bottom: 0;
    width: 880px;
    height: 46px;
  }
</style>
</head>
<body>
  <div class="business-card">
    <div class="accent-bar-left"></div>
    <div class="brand">
      <span class="brand-dot"></span>
      <span class="brand-name">
        <span class="primary">Brennick</span>
        <span class="secondary">Quality Solutions</span>
      </span>
    </div>
    <div class="name-bar">
      <div class="person-name">Marion Brennick</div>
      <div class="person-title">Principal Consultant</div>
    </div>
    <div class="contact">
      <div class="address">4817 Thistlewood<br>Lane Cary, NC 27604</div>
      <div class="line">Cell : 919-555-0148</div>
      <div class="line">marion@brennickquality.example</div>
      <div class="line">www.brennickquality.example</div>
    </div>
    <svg class="footer-bands" viewBox="0 0 880 46" aria-hidden="true">
      <polygon points="0,8 715,8 700,46 0,46" fill="var(--teal)"/>
      <polygon points="735,0 880,0 880,46 712,46" fill="var(--orange)"/>
    </svg>
  </div>
</body>
</html>
```